Orrin Computer Solutions Postcard Marketing Campaign

We need a postcard that markets to a wide range of clients including business and residential clients. We are open to all design ideas and colors, however our website is more black, blue, and white. We offer free initial consultations and subscription based service packages. Here is some information pulled off our website, Orrincomputer.net that will give a more general overview of our company:We at Orrin Computer Solutions strive for the highest customer satisfaction. Our aim is to be the best in the business not only on technical issues, but in exceeding customer expectations as well. We are a family owned and operated company located in New Braunfels, TX. We serve clients from San Antonio to Austin and everywhere in between. We understand the small business budget conscious approach and will always recommend and implement solutions around this model. Our goal is to help our clients further their businesses efficiency and effectiveness. At just over 15 years in the IT business we have seen just how important the right technology can be. We will never give in to a one size fits all approach and will always strive to match the technology to the customers needs.
Target Market(s)
small business <10 employees
residential
Industry/Entity Type
Information Technology
Look and feel

```html
<!DOCTYPE html>
<html lang="en">
<head>
<meta charset="utf-8">
<title>Orrin Computer Solutions Postcard</title>
<link rel="stylesheet" href="https://fonts.googleapis.com/css2?family=Oswald:wght@400;500;600&family=Open+Sans:wght@400;600&display=swap">
<style>
  :root {
    --backdrop: #5b5d60;
    --navy: #0f2438;
    --deep-blue: #1d4f8c;
    --stripe-blue: #1f4d91;
    --sky: #8fc3e8;
    --bar-dark: #2a2c30;
    --pill-dark: #2b2f36;
    --white: #ffffff;
    --ink: #1b2530;
    --line-blue: #7fa6cf;
  }
  * { margin: 0; padding: 0; box-sizing: border-box; }
  html, body { width: 758px; height: 1200px; overflow: hidden; }
  body {
    background: var(--backdrop);
    font-family: "Open Sans", Arial, sans-serif;
    position: relative;
  }
  .postcard {
    position: absolute;
    left: 30px;
    width: 698px;
    height: 574px;
    overflow: hidden;
    box-shadow: 0 6px 18px rgba(0,0,0,0.55);
  }
  .postcard--front { top: 13px; }
  .postcard--back { top: 614px; background: var(--white); }

  /* Front */
  .front-photo {
    position: absolute; inset: 0;
    background:
      radial-gradient(ellipse at 30% 35%, rgba(160,200,230,0.55), transparent 55%),
      radial-gradient(ellipse at 75% 60%, rgba(120,170,210,0.35), transparent 50%),
      linear-gradient(135deg, #27435f 0%, #1a2f46 45%, #2f5a80 100%);
  }
  .brand-front { position: absolute; left: 300px; top: 58px; width: 380px; text-align: center; color: var(--white); }
  .brand-front__name { font-family: "Oswald", sans-serif; font-weight: 500; font-size: 56px; letter-spacing: 5px; line-height: 1; }
  .brand-front__tag { font-family: "Oswald", sans-serif; font-weight: 400; font-size: 30px; letter-spacing: 2px; margin-top: 40px; }
  .offer { position: absolute; left: 72px; top: 355px; color: var(--white); line-height: 1.15; text-shadow: 0 1px 3px rgba(0,0,0,0.6); }
  .offer__lead { font-size: 22px; }
  .offer__main { font-size: 26px; }
  .contact-bar {
    position: absolute; left: 0; right: 0; bottom: 0; height: 96px;
    background: var(--bar-dark);
    display: flex; align-items: center; gap: 80px; padding-left: 48px;
    color: var(--white); font-size: 26px;
  }
  .contact { display: flex; align-items: center; gap: 14px; }
  .contact svg { flex: none; }

  /* Back */
  .back-photo {
    position: absolute; left: 0; top: 0; width: 410px; height: 574px;
    clip-path: polygon(0 0, 400px 0, 311px 574px, 0 574px);
    background:
      radial-gradient(ellipse at 30% 70%, rgba(210,230,245,0.9), transparent 60%),
      linear-gradient(160deg, #5f7f99 0%, #9fb8cb 45%, #2e4d6b 100%);
  }
  .back-stripe { position: absolute; left: 0; top: 0; }
  .brand-back { position: absolute; left: 30px; top: 44px; width: 280px; text-align: center; color: var(--navy); }
  .brand-back__name { font-family: "Oswald", sans-serif; font-weight: 600; font-size: 46px; letter-spacing: 4px; line-height: 1; }
  .brand-back__tag { font-family: "Oswald", sans-serif; font-weight: 500; font-size: 27px; letter-spacing: 1px; margin-top: 10px; }
  .services-title {
    position: absolute; left: 0; top: 157px; width: 300px; height: 32px;
    background: linear-gradient(90deg, transparent, var(--pill-dark) 20%, var(--pill-dark));
    color: var(--white); font-family: "Oswald", sans-serif; font-size: 21px;
    display: flex; align-items: center; justify-content: flex-end; padding-right: 22px;
  }
  .services { position: absolute; left: 0; top: 212px; list-style: none; }
  .services li {
    height: 30px; width: 200px; margin-bottom: 36px;
    background: var(--pill-dark); color: var(--white);
    border-radius: 0 15px 15px 0;
    font-size: 17px; display: flex; align-items: center; padding-left: 22px;
  }
  .back-contacts { position: absolute; left: 28px; top: 440px; color: var(--white); }
  .back-contacts .contact { font-size: 24px; margin-bottom: 14px; }
  .back-contacts .contact--email { font-size: 19px; }
  .stamp-box { position: absolute; left: 531px; top: 33px; width: 136px; height: 134px; border: 2px solid var(--deep-blue); }
  .address-lines { position: absolute; left: 398px; top: 248px; width: 268px; list-style: none; }
  .address-lines li { height: 37px; border-bottom: 2px solid var(--line-blue); }
</style>
</head>
<body>

<section class="postcard postcard--front">
  <div class="front-photo" role="img" aria-label="Photo of a businessman in a suit touching a glowing digital interface with data icons and a world map"></div>
  <div class="brand-front">
    <div class="brand-front__name">ORRIN</div>
    <div class="brand-front__tag">COMPUTER SOLUTIONS</div>
  </div>
  <div class="offer">
    <div class="offer__lead">Call or Email</div>
    <div class="offer__lead">Today For a</div>
    <div class="offer__main">Free Consultation</div>
  </div>
  <div class="contact-bar">
    <div class="contact">
      <svg width="34" height="40" viewBox="0 0 34 40" aria-hidden="true"><path d="M10 4 L15 12 L11 16 Q14 24 20 28 L24 24 L31 30 L26 36 Q12 34 5 18 Q3 10 10 4 Z" fill="#fff"/></svg>
      <span>830-555-0148</span>
    </div>
    <div class="contact">
      <svg width="34" height="26" viewBox="0 0 34 26" aria-hidden="true"><rect x="2" y="2" width="30" height="22" fill="none" stroke="#fff" stroke-width="2.5"/><path d="M2 3 L17 15 L32 3" fill="none" stroke="#fff" stroke-width="2.5"/></svg>
      <span>Cal@Orrincomputer.net</span>
    </div>
  </div>
</section>

<section class="postcard postcard--back">
  <div class="back-photo" role="img" aria-label="Photo of a digital globe with a glowing world map"></div>
  <svg class="back-stripe" width="420" height="574" aria-hidden="true"><polygon points="400,0 414,0 325,574 311,574" fill="var(--stripe-blue)"/></svg>
  <div class="brand-back">
    <div class="brand-back__name">ORRIN</div>
    <div class="brand-back__tag">COMPUTER SOLUTIONS</div>
  </div>
  <div class="services-title">IT Solutions Provided</div>
  <ul class="services">
    <li>Residential Solutions</li>
    <li>Business Solutions</li>
    <li>Remote Solutions</li>
  </ul>
  <div class="back-contacts">
    <div class="contact">
      <svg width="30" height="36" viewBox="0 0 34 40" aria-hidden="true"><path d="M10 4 L15 12 L11 16 Q14 24 20 28 L24 24 L31 30 L26 36 Q12 34 5 18 Q3 10 10 4 Z" fill="#fff"/></svg>
      <span>830-555-0148</span>
    </div>
    <div class="contact contact--email">
      <svg width="28" height="22" viewBox="0 0 34 26" aria-hidden="true"><rect x="2" y="2" width="30" height="22" fill="none" stroke="#fff" stroke-width="2.5"/><path d="M2 3 L17 15 L32 3" fill="none" stroke="#fff" stroke-width="2.5"/></svg>
      <span>Cal@Orrincomputer.net</span>
    </div>
  </div>
  <div class="stamp-box"></div>
  <ul class="address-lines">
    <li></li><li></li><li></li><li></li><li></li>
  </ul>
</section>

</body>
</html>
```